Letterhead for denture company

We need a letterhead designed for our denture company called "Brightbite" We have attached the logo and business card with the colours on them that we like

Target Market(s)

Everyone aged 45+

Industry/Entity Type

Dental Clinic

Font styles to use
Serif
Sans Serif

Colors
3276b5
f37122

Requirements
Must have
• The colours used in our business card
• Be bold and modern
• Thick fonts
• Logo
Nice to have
• Elements that could tie in nicely with any future signage or website upgrades
Should not have
• Thin font
• Should not be too busy

```html
<!DOCTYPE html>
<html lang="en">
<head>
<meta charset="utf-8">
<title>Brightbite Letterhead</title>
<link rel="stylesheet" href="https://fonts.googleapis.com/css2?family=Exo+2:wght@400;600;700&display=swap">
<style>
  :root {
    --brand-blue: #0a72ba;
    --accent-orange: #dd6a35;
    --paper: #ffffff;
  }
  * { margin: 0; padding: 0; box-sizing: border-box; }
  html, body { width: 891px; height: 1200px; overflow: hidden; background: var(--paper); }
  .letterhead {
    position: relative;
    width: 891px;
    height: 1200px;
    background: var(--paper);
    font-family: "Exo 2", sans-serif;
  }
  .masthead {
    position: absolute;
    top: 31px;
    left: 0;
    width: 100%;
    display: flex;
    flex-direction: column;
    align-items: center;
  }
  .masthead__mark {
    width: 66px;
    height: 63px;
    background: var(--brand-blue);
    border-radius: 3px;
  }
  .masthead__name {
    margin-top: 4px;
    padding-left: 4px;
    font-size: 35px;
    font-weight: 700;
    letter-spacing: 4px;
    line-height: 38px;
    color: var(--brand-blue);
    text-transform: uppercase;
  }
  .footer-band {
    position: absolute;
    left: 0;
    bottom: 0;
    width: 891px;
    height: 106px;
    display: block;
  }
  .footer-brand {
    position: absolute;
    left: 33px;
    top: 1137px;
    display: flex;
    align-items: center;
    gap: 9px;
  }
  .footer-brand__mark {
    width: 44px;
    height: 42px;
    background: var(--paper);
    border-radius: 2px;
  }
  .footer-brand__name {
    font-size: 23px;
    font-weight: 700;
    letter-spacing: 2.5px;
    color: var(--paper);
    text-transform: uppercase;
  }
  .footer-contact {
    position: absolute;
    top: 1139px;
    font-size: 12px;
    font-weight: 600;
    line-height: 14.5px;
    letter-spacing: 0.6px;
    color: var(--paper);
    font-style: normal;
  }
  .footer-contact--address { left: 452px; }
  .footer-contact--phone { left: 687px; }
  .footer-contact b { font-weight: 700; }
</style>
</head>
<body>
  <main class="letterhead">
    <header class="masthead">
      <div class="masthead__mark" aria-hidden="true"></div>
      <div class="masthead__name">Brightbite</div>
    </header>

    <svg class="footer-band" viewBox="0 0 891 106" aria-hidden="true">
      <rect x="0" y="14" width="596" height="8" fill="var(--accent-orange)"/>
      <path d="M0,25 L592,25 C600,25 604,22 608,16 L615,6 C619,1 622,0 630,0 L891,0 L891,106 L0,106 Z" fill="var(--brand-blue)"/>
    </svg>

    <div class="footer-brand">
      <div class="footer-brand__mark" aria-hidden="true"></div>
      <div class="footer-brand__name">Brightbite</div>
    </div>

    <address class="footer-contact footer-contact--address">
      48 Harbour View Road<br>
      Riverside North, Auckland 0612<br>
      www.brightbite.co.nz
    </address>
    <address class="footer-contact footer-contact--phone">
      <b>P:</b> 0800 55 1234<br>
      <b>C:</b> 09 555 0142<br>
      hello@brightbite.co.nz
    </address>
  </main>
</body>
</html>
```